Simple, bright, clean website - 3 pages, easy to update with WordPress!

I want to update my website (brelvatix.com) with a brighter/cleaner interface. It is quite dark right now. I would like it to be similar to a partner site (https://www.nodavent-44.com/). White with some orange highlights (matching the logo). I want to be able to easily update the site content. There should be 3 main pages: About, Services, Contact. I also like a design similar to quorfen.com

Target Market(s)

Anyone using technology to achieve business goals.

Industry/Entity Type

Managed Service Provider (IT)

Coding

Coded - Design and coding required

Number of Pages Required

3 page

Colors
F0912C
F2A743
F7CA91
FBE8D2
FDF5EE

Requirements
Must have
• Links to standard social media apps like WorkLattice, Pallgrove, etc.. Easy to edit and add pages.

```html
<!DOCTYPE html>
<html lang="en">
<head>
<meta charset="utf-8">
<title>Brelvatix Consulting Inc. — Trusted Technology Solutions</title>
<link rel="stylesheet" href="https://fonts.googleapis.com/css2?family=Poppins:wght@300;400;500;600;700&display=swap">
<style>
:root{
  --orange:#F0912C;
  --amber:#F2A743;
  --sand:#F7CA91;
  --cream:#FBE8D2;
  --ivory:#FDF5EE;
  --ink:#2b2b2b;
  --text:#555;
  --grey:#7c7c7c;
  --dark:#3e3e3e;
  --badge:#1d2a2a;
}
*{box-sizing:border-box;margin:0;padding:0}
html,body{width:1200px;height:4173px;overflow:hidden}
body{font-family:"Poppins",sans-serif;color:var(--text);background:#fff;position:relative}
.abs{position:absolute}
.section{position:absolute;left:0;width:1200px}

/* header */
.site-header{top:0;height:139px;background:#fff}
.brand{left:85px;top:38px;font-size:54px;font-weight:500;color:var(--grey);line-height:1}
.badge-placeholder{left:392px;top:0;width:136px;height:136px;border-radius:50%;background:var(--badge)}
.btn-pill{display:flex;align-items:center;justify-content:center;gap:8px;border-radius:20px;color:#fff;font-size:14px;font-weight:600;height:38px}
.btn-login{left:717px;top:34px;width:178px;background:#4a4a4a}
.btn-connect{left:907px;top:34px;width:207px;background:var(--amber)}
.main-nav{left:700px;top:88px;display:flex;font-size:14px;color:#444}
.main-nav a{text-decoration:none;color:inherit;margin-right:38px;padding:4px 10px 8px}
.main-nav a.active{color:var(--orange);border-bottom:2px solid var(--orange)}

/* hero */
.hero{top:139px;height:721px;background:radial-gradient(ellipse at 50% 75%,#6b4b22 0%,#2b1f12 40%,#0b0b0d 80%)}
.hero-power{left:565px;top:132px}
.hero-title{top:232px;width:1200px;text-align:center;color:#fff;font-weight:700;font-size:72px;line-height:86px;letter-spacing:1px}
.btn-hero{left:491px;top:439px;width:219px;height:60px;border-radius:30px;background:var(--amber);color:#fff;font-weight:600;font-size:17px;display:flex;align-items:center;justify-content:center}
.dots{left:563px;top:642px;display:flex;gap:5px}
.dots span{width:15px;height:15px;border-radius:50%;background:#999}
.dots span:first-child{background:#fff}

/* shared heading */
.heading{width:1200px;text-align:center}
.heading h2{font-size:46px;font-weight:500;color:var(--amber);line-height:1}
.heading p{font-size:24px;font-weight:300;letter-spacing:5px;color:#9a9a9a;margin-left:140px;line-height:1.3}

/* about */
.about{top:860px;height:670px;background:var(--ivory)}
.about-frame{left:135px;top:100px;width:422px;height:467px;background:var(--amber)}
.about-photo{left:157px;top:120px;width:421px;height:466px;background:linear-gradient(160deg,#d9d6cf,#a8a6a0 55%,#ecebe7)}
.about-line{left:164px;top:127px;width:392px;height:440px;border:1.5px solid #fff}
.about-heading{left:643px;top:156px}
.about-heading h2{font-size:43px;font-weight:500;color:var(--amber);line-height:1}
.about-heading p{font-size:21px;font-weight:300;letter-spacing:4px;color:#9a9a9a;margin-left:38px}
.about-copy{left:643px;top:250px;width:422px;font-size:15px;line-height:31px;text-align:justify;color:#555}
.btn-solid{border-radius:30px;background:var(--amber);color:#fff;font-weight:500;font-size:15px;display:flex;align-items:center;justify-content:center}
.btn-know{left:643px;top:469px;width:187px;height:57px}

/* services */
.services{top:1530px;height:970px;background:#fff}
.services .heading{top:110px}
.services-intro{top:205px;left:140px;width:920px;text-align:center;font-size:15px;line-height:31px;color:#444}
.service-card{position:absolute;width:316px;height:268px}
.service-img{position:absolute;left:0;top:0;width:316px;height:233px}
.service-label{position:absolute;left:26px;top:198px;width:265px;height:70px;background:#fff;box-shadow:0 2px 10px rgba(0,0,0,.12);display:flex;align-items:center;justify-content:center;text-align:center;font-size:17px;font-weight:500;color:#333;line-height:1.2}
.service-label.highlight{background:var(--amber);color:#fff}
.slider-arrow{position:absolute;width:48px;height:48px;border-radius:50%;display:flex;align-items:center;justify-content:center}

/* testimonials */
.testimonials{top:2500px;height:562px;background:var(--ivory)}
.testimonials .heading{top:100px}
.review{position:absolute;top:236px;width:340px}
.avatar{position:absolute;left:0;top:0;width:90px;height:90px;border-radius:50%;background:linear-gradient(150deg,#d8d4ce,#8e8a85);border:3px solid #fff}
.review-body{position:absolute;left:112px;top:0;width:216px}
.quote{color:var(--amber);font-size:26px;font-weight:700;line-height:14px;float:left;margin-right:18px;font-family:Georgia,serif}
.review-text{font-size:11.5px;line-height:19.5px;color:#444;text-align:justify}
.review-name{font-size:14px;font-weight:600;color:#222;margin-top:22px}
.stars{color:var(--amber);font-size:11px;letter-spacing:1px}

/* contact */
.contact{top:3062px;height:1038px;background:#fff}
.contact .heading{top:98px}
.contact-band{left:0;top:605px;width:1200px;height:433px;background:var(--amber)}
.contact-bar{left:232px;top:223px;width:740px;height:7px;background:var(--amber)}
.contact-card{left:220px;top:230px;width:763px;height:592px;background:var(--ivory)}
.field{position:absolute;left:51px;width:332px;background:#fff;box-shadow:0 2px 6px rgba(0,0,0,.08);font-size:15px;color:#aaa;padding:15px 23px}
.btn-submit{left:51px;top:360px;width:186px;height:57px;font-size:15px}
.info{position:absolute;left:428px;display:flex;gap:24px}
.info-icon{width:35px;height:35px;border-radius:4px;background:var(--amber);display:flex;align-items:center;justify-content:center;flex:none;margin-top:6px}
.info-label{font-size:17px;color:var(--amber);line-height:1.2}
.info-value{font-size:17px;color:#333;line-height:1.2}

/* footer */
.footer-brand{top:850px;width:1200px;text-align:center;color:#fff;font-size:64px;font-weight:500;line-height:1}
.footer-rule{left:90px;top:958px;width:1030px;height:1px;background:rgba(255,255,255,.5)}
.footer-nav{top:983px;width:1200px;display:flex;justify-content:center;color:#fff;font-size:15px}
.footer-nav span{padding:0 34px}
.bottom-bar{top:4100px;height:73px;background:var(--dark);color:#fff}
.copyright{left:89px;top:27px;font-size:13px}
.social{left:962px;top:15px;display:flex;gap:6px}
.social a{display:block;width:35px;height:35px;border:1.5px solid #fff;border-radius:3px}
</style>
</head>
<body>

<header class="section site-header">
  <div class="abs brand">Brelvatix</div>
  <div class="abs badge-placeholder" role="img" aria-label="Anniversary badge"></div>
  <a class="abs btn-pill btn-login">
    <svg width="16" height="16" viewBox="0 0 16 16"><circle cx="8" cy="5" r="3.5" fill="#fff"/><path d="M1 16c0-4 3-6 7-6s7 2 7 6z" fill="#fff"/></svg>
    CLIENT LOGIN
  </a>
  <a class="abs btn-pill btn-connect">
    <svg width="18" height="18" viewBox="0 0 18 18" fill="none" stroke="#fff" stroke-width="2"><path d="M7 11l4-4"/><path d="M9 4l2-2a3 3 0 014 4l-2 2"/><path d="M9 14l-2 2a3 3 0 01-4-4l2-2"/></svg>
    CONNECT MY TECH
  </a>
  <nav class="abs main-nav">
    <a class="active">HOME</a><a>ABOUT US</a><a>SERVICES</a><a>CONTACT US</a>
  </nav>
</header>

<section class="section hero" role="img" aria-label="City skyline at night with an illuminated arena in the foreground">
  <svg class="abs hero-power" width="70" height="90" viewBox="0 0 70 90" fill="none" stroke="#F2A743" stroke-width="4" stroke-linecap="round">
    <path d="M35 2v34"/><path d="M20 26a28 28 0 1030 0"/>
  </svg>
  <h1 class="abs hero-title">YOUR PARTNER IN TRUSTED<br>TECHNOLOGY SOLUTIONS</h1>
  <a class="abs btn-hero">CONTACT US</a>
  <div class="abs dots"><span></span><span></span><span></span><span></span></div>
</section>

<section class="section about">
  <div class="abs about-frame"></div>
  <div class="abs about-photo" role="img" aria-label="Smiling businesswoman in glasses seated at a laptop"></div>
  <div class="abs about-line"></div>
  <div class="abs about-heading">
    <h2>About Us</h2>
    <p>Who we Are</p>
  </div>
  <p class="abs about-copy">Lorem ipsum dolor sit amet, consectetur adipiscing elit. Etiam in vestibulum urna. Quisque in lectus non sem consequat varius mattis id odio. Mauris sed libero a velit pellentesque volutpat. Donec sed augue congue, consequat eros in, fringilla ante. Interdum et malesua da fames ac ante ipsum primis in faucibus.</p>
  <a class="abs btn-solid btn-know">KNOW MORE</a>
</section>

<section class="section services">
  <div class="abs heading"><h2>Our Services</h2><p>What We Do</p></div>
  <p class="abs services-intro">Lorem ipsum dolor sit amet, consectetur adipiscing elit. Etiam in vestibulum urna. Quisque in lectus non sem conse quat varius mattis id odio. Mauris sed libero a velit pellentesque volutpat. Donec sed augue congue,</p>

  <div class="service-card" style="left:100px;top:307px">
    <div class="service-img" role="img" aria-label="Dark server room with network overlay" style="background:linear-gradient(160deg,#4a4a4a,#1c1c1c)"></div>
    <div class="service-label">Managed IT Services</div>
  </div>
  <div class="service-card" style="left:443px;top:307px">
    <div class="service-img" role="img" aria-label="Team of colleagues gathered around a laptop" style="background:linear-gradient(160deg,#cfc8bd,#6f6458)"></div>
    <div class="service-label highlight">IT Consulting</div>
  </div>
  <div class="service-card" style="left:784px;top:307px">
    <div class="service-img" role="img" aria-label="Glowing cloud above a digital grid" style="background:linear-gradient(160deg,#6fa3b8,#143248)"></div>
    <div class="service-label">Cloud Services<br>including VoIP</div>
  </div>
  <div class="service-card" style="left:100px;top:617px">
    <div class="service-img" role="img" aria-label="Support agent with headset at a desk" style="background:linear-gradient(160deg,#8e8576,#3a3430)"></div>
    <div class="service-label">24/7 Helpdesk</div>
  </div>
  <div class="service-card" style="left:443px;top:617px">
    <div class="service-img" role="img" aria-label="Computers and devices with network icons" style="background:linear-gradient(160deg,#3d78b4,#0e2746)"></div>
    <div class="service-label">Hardware/Softwar<br>procurement</div>
  </div>
  <div class="service-card" style="left:784px;top:617px">
    <div class="service-img" role="img" aria-label="Hand touching a digital padlock screen" style="background:linear-gradient(160deg,#7fa6cc,#2a4f7d)"></div>
    <div class="service-label">Security and Backup<br>Solutions</div>
  </div>

  <div class="slider-arrow" style="left:14px;top:560px;background:#9a9a9a">
    <svg width="14" height="14" viewBox="0 0 14 14" fill="none" stroke="#fff" stroke-width="2.5"><path d="M9 2L4 7l5 5"/></svg>
  </div>
  <div class="slider-arrow" style="left:1138px;top:560px;background:var(--amber)">
    <svg width="14" height="14" viewBox="0 0 14 14" fill="none" stroke="#fff" stroke-width="2.5"><path d="M5 2l5 5-5 5"/></svg>
  </div>
</section>

<section class="section testimonials">
  <div class="abs heading"><h2>Our Testimonials</h2><p>Client Reviews</p></div>

  <div class="review" style="left:85px">
    <div class="avatar" role="img" aria-label="Client portrait"></div>
    <div class="review-body">
      <p class="review-text"><span class="quote">“</span>Lorem ipsum dolor sit amet, consectetur adipiscing elit. Maece nas ac tellus ac ipsum porta viverra sit amet sed leo. Vivamus eu mauris convallis, hendrerit</p>
      <p class="review-name">Dara Vellen</p>
      <p class="stars">★★★★★</p>
    </div>
  </div>
  <div class="review" style="left:438px">
    <div class="avatar" role="img" aria-label="Client portrait"></div>
    <div class="review-body">
      <p class="review-text"><span class="quote">“</span>Lorem ipsum dolor sit amet, consectetur adipiscing elit. Maece nas ac tellus ac ipsum porta viverra sit amet sed leo. Vivamus eu mauris convallis, hendrerit</p>
      <p class="review-name">Marlow Pennick</p>
      <p class="stars">★★★★★</p>
    </div>
  </div>
  <div class="review" style="left:791px">
    <div class="avatar" role="img" aria-label="Client portrait"></div>
    <div class="review-body">
      <p class="review-text"><span class="quote">“</span>Lorem ipsum dolor sit amet, consectetur adipiscing elit. Maece nas ac tellus ac ipsum porta viverra sit amet sed leo. Vivamus eu mauris convallis, hendrerit</p>
      <p class="review-name">Joren Saltby</p>
      <p class="stars">★★★★★</p>
    </div>
  </div>

  <div class="slider-arrow" style="left:548px;top:436px;background:#9a9a9a">
    <svg width="14" height="14" viewBox="0 0 14 14" fill="none" stroke="#fff" stroke-width="2.5"><path d="M9 2L4 7l5 5"/></svg>
  </div>
  <div class="slider-arrow" style="left:603px;top:436px;background:var(--amber)">
    <svg width="14" height="14" viewBox="0 0 14 14" fill="none" stroke="#fff" stroke-width="2.5"><path d="M5 2l5 5-5 5"/></svg>
  </div>
</section>

<section class="section contact">
  <div class="abs heading"><h2>Contact Us</h2><p>Get In touch</p></div>
  <div class="abs contact-band"></div>
  <div class="abs contact-bar"></div>
  <div class="abs contact-card">
    <div class="field" style="top:70px;height:52px">Name*</div>
    <div class="field" style="top:144px;height:52px">E-Mail*</div>
    <div class="field" style="top:222px;height:105px">Messages</div>
    <a class="abs btn-solid btn-submit">SUBMIT NOW</a>

    <div class="info" style="top:108px">
      <div class="info-icon"><svg width="16" height="16" viewBox="0 0 16 16"><path d="M4 1l2 3-1.5 1.5a8 8 0 006 6L12 10l3 2-1.5 3C7 15 1 9 1 2.5z" fill="#fff"/></svg></div>
      <div><p class="info-label">CALL US</p><p class="info-value">8012 555 0147</p></div>
    </div>
    <div class="info" style="top:175px">
      <div class="info-icon"><svg width="16" height="12" viewBox="0 0 16 12"><rect width="16" height="12" rx="1" fill="#fff"/><path d="M1 1l7 5 7-5" fill="none" stroke="#F2A743" stroke-width="1.5"/></svg></div>
      <div><p class="info-label">EMAIL US</p><p class="info-value">hello@brelvatix.com</p></div>
    </div>
    <div class="info" style="top:243px">
      <div class="info-icon"><svg width="14" height="18" viewBox="0 0 14 18"><path d="M7 0a7 7 0 017 7c0 5-7 11-7 11S0 12 0 7a7 7 0 017-7z" fill="#fff"/><circle cx="7" cy="7" r="2.5" fill="#F2A743"/></svg></div>
      <div><p class="info-value">Address line Dummy Here<br>Address line Here</p></div>
    </div>
  </div>

  <div class="abs footer-brand">Brelvatix</div>
  <div class="abs footer-rule"></div>
  <nav class="abs footer-nav">
    <span>HOME</span>|<span>ABOUT US</span>|<span>SERVICES</span>|<span>CONTACT US</span>
  </nav>
</section>

<footer class="section bottom-bar">
  <p class="abs copyright">Copyright © 2024 All Rights Reserved By Company name</p>
  <div class="abs social">
    <a aria-label="Pallgrove"></a><a aria-label="Social link"></a><a aria-label="Social link"></a><a aria-label="WorkLattice"></a>
  </div>
</footer>

</body>
</html>
```